Infectious Diseases Research Laboratory Needs Business Card

We need a business card for an academic research laboratory based in Kansas City called VELKOR. The full lab name is Microbe Exposure Kinetics/Response Modeling Integrated Study Laboratory, but this does not need to be incorporated. We study novel ways to optimize the treatment of multidrug-resistant bacterial infections ("superbugs") throughout the entire biomedical research spectrum (from benchtop to bedside). The name VELKOR is not only an acronym for our lab name, but also represents our desire to make discoveries and explore the unknown (the stars, if you well). It also serves as an ode to the state of Kansas motto where we are based, ad astra per aspera ("to the stars, through difficulty").

Target Market(s)

Pharmaceutical companies, researchers

Industry/Entity Type

Pharmaceutical

Contact Information for Business Card

The business card should incorporate and complement our new logo (see uploaded files). Double-sided designs are preferred. Looking for something modern, but professional.

Font styles to use
Sans Serif

Requirements
Must have
• Double-sided. One side would ideally be a solid color incorporating logo and the other should also have the logo (smaller), but incorporate staff information.
• Color codes:
• Red: #F04C51
• Blue: #3477B5
• Gray: #808285

```html
<!DOCTYPE html>
<html lang="en">
<head>
<meta charset="UTF-8">
<title>VELKOR Business Card</title>
<link href="https://fonts.googleapis.com/css2?family=Montserrat:wght@400;500;700&display=swap" rel="stylesheet">
<style>
  :root {
    --red: #F04C51;
    --blue: #3477B5;
    --paper: #f2f2f1;
    --paper-shade: #e2e2e0;
    --white: #ffffff;
    --backdrop: #e8e5e1;
  }
  * { margin: 0; padding: 0; box-sizing: border-box; }
  html, body {
    width: 1200px;
    height: 900px;
    overflow: hidden;
    background: var(--backdrop);
    font-family: "Montserrat", Arial, sans-serif;
  }
  .card {
    position: absolute;
    left: 120px;
    top: 153px;
    width: 960px;
    height: 593px;
    background: var(--red);
    overflow: hidden;
    box-shadow: 0 10px 30px rgba(0,0,0,0.15);
  }
  .card__band {
    position: absolute;
    left: 678px;
    top: 0;
    width: 282px;
    height: 100%;
    background: var(--blue);
  }
  .card__disc {
    position: absolute;
    left: 425px;
    top: 64px;
    width: 466px;
    height: 466px;
    border-radius: 50%;
    background: radial-gradient(circle at 40% 35%, var(--white) 0%, var(--paper) 55%, var(--paper-shade) 100%);
    display: flex;
    align-items: center;
    justify-content: center;
    gap: 16px;
  }
  .brand__dot {
    width: 44px;
    height: 44px;
    border-radius: 50%;
    background: var(--blue);
  }
  .brand__name {
    font-weight: 500;
    font-size: 66px;
    letter-spacing: 4px;
    color: var(--red);
    line-height: 1;
  }
  .person {
    position: absolute;
    left: 54px;
    top: 52px;
    color: var(--white);
  }
  .person__name {
    font-weight: 700;
    font-size: 33px;
    letter-spacing: 0.5px;
    line-height: 1.1;
  }
  .person__role {
    font-weight: 400;
    font-size: 24px;
    line-height: 1.2;
  }
  .contact {
    position: absolute;
    left: 54px;
    top: 356px;
    list-style: none;
    color: var(--white);
    font-size: 24px;
    line-height: 35px;
  }
  .contact__item {
    display: flex;
    align-items: center;
    gap: 12px;
  }
  .contact__icon {
    width: 16px;
    height: 16px;
    fill: var(--white);
    flex: none;
  }
  .address {
    position: absolute;
    left: 54px;
    top: 477px;
    color: var(--white);
    font-size: 24px;
    line-height: 35px;
    font-style: normal;
  }
</style>
</head>
<body>
  <main class="card">
    <div class="card__band"></div>

    <div class="person">
      <h1 class="person__name">MARCUS HALE</h1>
      <p class="person__role">Managing Director</p>
    </div>

    <ul class="contact">
      <li class="contact__item">
        <svg class="contact__icon" viewBox="0 0 16 16" aria-hidden="true"><path d="M3.5 1l2.5 3-1.5 2c1 2 3 4 5 5l2-1.5 3 2.5-1.5 2.5C7 14 2 9 1 2.5z"/></svg>
        <span>(816)555-0142</span>
      </li>
      <li class="contact__item">
        <svg class="contact__icon" viewBox="0 0 16 16" aria-hidden="true"><path d="M1 3h14v10H1z M1 3l7 6 7-6" fill="var(--white)" stroke="var(--red)" stroke-width="1.2"/></svg>
        <span>info@velkorlab.org</span>
      </li>
      <li class="contact__item">
        <svg class="contact__icon" viewBox="0 0 16 16" aria-hidden="true"><circle cx="8" cy="8" r="7"/><path d="M1 8h14M8 1c-3 3-3 11 0 14M8 1c3 3 3 11 0 14" fill="none" stroke="var(--red)" stroke-width="1"/></svg>
        <span>www.velkorlab.org</span>
      </li>
    </ul>

    <address class="address">
      2410, Holmes Street,<br>
      Kansas City, 64108
    </address>

    <div class="card__disc">
      <span class="brand__dot"></span>
      <span class="brand__name">VELKOR</span>
    </div>
  </main>
</body>
</html>
```